Design for "Quiver" protein health bars wrappers

I need a new design for a protein bar that my partners and I are launching for the North American and European markets.
The bar's name is "Quiver."
Given the masculine/aggressive nature of that name, we are thinking of neutralizing it with a more feminine/soft font and design. But hey - the sky is the limit. We obviously want this 20-gram protein bar to sell to a wide net (not just men but women also). So if it means having a Zephyr Panel font/design (or whatever) in order to do this, so be it. I leave it up to your intelligence and experience.

The official name of the bar is just "QUIVER" (not "Quiver Protein").

We have six flavors divided into two categories, which are 1) SOFT and 2) CRUNCHY.
So, the idea is to make two similar designs for the wrapper that still distinguish themselves from each other because one is 'soft' and the other is 'crunchy.'
Then, within each category, the idea is to have three color variations, designating the three flavors in each category.

Please look at the dimensions and examples of the generic wrapper designs that we already have (and which we find too generic), which I have uploaded.

Target Market(s)

North America - Valmart, Green Basket
Europe - Norway, Sweden, Denmark, Germany, France, Switzerland, Italy.

Industry/Entity Type

Nutrition

Logo Text

Quiver

Font styles to use
Serif
Decorative

Colors
fff6dc
f04a50

Requirements
Must have
• The title is "Quiver".
• We have six flavors divided into two categories, which are 1) SOFT and 2) CRUNCHY.
• You can work on the two different types of similar-but-different designs for the "soft" and for the "cruncy." Then it's just a question of color variations for each flavor.
• The flavors are:
• SOFT: 1) strawberry, 2) Chocolate brownie, 3) Cinnamon Crunch
• CRUNCY: 1) Peanut, 2) Lemon, 3) Coconut.
• On the side or at the bottom, there should be stated:
• "20 gm protein"
• "children friendly"
Nice to have
• Obvious: a design that catches the eye and inspires someone to buy the bar to eat it.
• Part of the design could include a photograph of the actual bar (you can use generic photos for that until we place a pic of the actual bar). Like 1/4th of the total surface (or even a little smaller).

```html
<!DOCTYPE html>
<html lang="en">
<head>
<meta charset="utf-8">
<title>Quiver Crunchy Lemon Wrapper</title>
<link rel="stylesheet" href="https://fonts.googleapis.com/css2?family=Bebas+Neue&family=Rozha+One&family=Roboto:wght@500;700&display=swap">
<style>
  :root {
    --page-bg: #ececec;
    --wrapper-yellow: #e9bd22;
    --wrapper-brown: #2a1011;
    --band-white: #ffffff;
    --text-white: #ffffff;
    --crimp-line: #8a8272;
    --lemon-light: #f7e27a;
    --lemon-deep: #e8c21c;
  }
  * { margin: 0; padding: 0; box-sizing: border-box; }
  html, body {
    width: 1200px; height: 1039px; overflow: hidden;
    background: var(--page-bg);
  }
  .wrapper {
    position: absolute; left: 142px; top: 307px;
    width: 915px; height: 424px;
    background: var(--wrapper-brown);
    overflow: hidden;
  }
  .top-band {
    position: absolute; left: 0; top: 0; width: 100%; height: 59px;
    background: var(--wrapper-yellow);
  }
  .logo-panel {
    position: absolute; left: 0; top: 0; width: 641px; height: 215px;
    background: var(--wrapper-yellow);
  }
  .category-band {
    position: absolute; left: 641px; top: 59px; width: 274px; height: 65px;
    background: var(--band-white);
  }
  .category-label {
    position: absolute; left: 684px; top: 73px;
    font-family: "Bebas Neue", sans-serif; font-size: 40px; line-height: 1;
    letter-spacing: 10px; color: var(--wrapper-brown);
  }
  .crimp {
    position: absolute; top: 0; width: 54px; height: 100%;
  }
  .crimp-left { left: 0; }
  .crimp-right { right: 0; }
  .brand-name {
    position: absolute; left: 88px; top: 27px;
    font-family: "Rozha One", serif; font-size: 176px; line-height: 1;
    font-weight: 400; color: var(--text-white); letter-spacing: -2px;
    white-space: nowrap;
    transform: scaleX(0.85); transform-origin: left top;
  }
  .flavour-name {
    position: absolute; left: 88px; top: 233px;
    font-family: "Bebas Neue", sans-serif; font-size: 68px; line-height: 1;
    font-weight: 400; color: var(--wrapper-yellow);
  }
  .claims {
    position: absolute; left: 90px; top: 307px;
    font-family: "Bebas Neue", sans-serif; font-size: 31px; line-height: 28px;
    color: var(--text-white); list-style: none;
  }
  .protein-badge {
    position: absolute; left: 527px; top: 249px; width: 112px; height: 104px;
    background: var(--wrapper-yellow); color: var(--text-white);
    font-family: "Roboto", sans-serif; text-align: center;
    display: flex; flex-direction: column; justify-content: center;
  }
  .protein-amount { font-size: 30px; font-weight: 700; line-height: 1.05; }
  .protein-label { font-size: 18px; font-weight: 500; line-height: 1.1; }
  .flavour-photo {
    position: absolute; left: 668px; top: 168px; width: 200px; height: 160px;
  }
  .photo-half {
    position: absolute; border-radius: 50%;
    background: radial-gradient(circle at 45% 45%, var(--lemon-light), var(--lemon-deep));
  }
  .photo-half.front { left: 0; top: 22px; width: 134px; height: 138px; }
  .photo-half.back { left: 106px; top: 0; width: 94px; height: 128px; }
</style>
</head>
<body>
  <div class="wrapper">
    <div class="top-band"></div>
    <div class="logo-panel"></div>
    <div class="category-band"></div>

    <svg class="crimp crimp-left" viewBox="0 0 54 424" aria-hidden="true">
      <g stroke="var(--crimp-line)" stroke-width="3" opacity="0.8">
        <line x1="8" x2="50" y1="22" y2="22"/><line x1="8" x2="50" y1="32" y2="32"/>
        <line x1="8" x2="50" y1="42" y2="42"/><line x1="8" x2="50" y1="52" y2="52"/>
        <line x1="8" x2="50" y1="62" y2="62"/><line x1="8" x2="50" y1="72" y2="72"/>
        <line x1="8" x2="50" y1="82" y2="82"/><line x1="8" x2="50" y1="92" y2="92"/>
        <line x1="8" x2="50" y1="102" y2="102"/><line x1="8" x2="50" y1="112" y2="112"/>
        <line x1="8" x2="50" y1="122" y2="122"/><line x1="8" x2="50" y1="132" y2="132"/>
        <line x1="8" x2="50" y1="142" y2="142"/><line x1="8" x2="50" y1="152" y2="152"/>
        <line x1="8" x2="50" y1="162" y2="162"/><line x1="8" x2="50" y1="172" y2="172"/>
        <line x1="8" x2="50" y1="182" y2="182"/><line x1="8" x2="50" y1="192" y2="192"/>
        <line x1="8" x2="50" y1="202" y2="202"/>
      </g>
    </svg>
    <svg class="crimp crimp-right" viewBox="0 0 54 424" aria-hidden="true">
      <g stroke="var(--crimp-line)" stroke-width="3" opacity="0.8">
        <line x1="4" x2="46" y1="22" y2="22"/><line x1="4" x2="46" y1="32" y2="32"/>
        <line x1="4" x2="46" y1="42" y2="42"/><line x1="4" x2="46" y1="52" y2="52"/>
        <line x1="4" x2="46" y1="62" y2="62"/><line x1="4" x2="46" y1="72" y2="72"/>
        <line x1="4" x2="46" y1="82" y2="82"/><line x1="4" x2="46" y1="92" y2="92"/>
        <line x1="4" x2="46" y1="102" y2="102"/><line x1="4" x2="46" y1="112" y2="112"/>
        <line x1="4" x2="46" y1="122" y2="122"/><line x1="4" x2="46" y1="132" y2="132"/>
        <line x1="4" x2="46" y1="142" y2="142"/><line x1="4" x2="46" y1="152" y2="152"/>
        <line x1="4" x2="46" y1="162" y2="162"/><line x1="4" x2="46" y1="172" y2="172"/>
        <line x1="4" x2="46" y1="182" y2="182"/><line x1="4" x2="46" y1="192" y2="192"/>
        <line x1="4" x2="46" y1="202" y2="202"/>
      </g>
    </svg>

    <span class="category-label">Crunchy</span>
    <h1 class="brand-name">QUIVER</h1>
    <h2 class="flavour-name">Lemon</h2>
    <ul class="claims">
      <li>Suitable for children</li>
      <li>Smooth protein – easily digestible</li>
    </ul>
    <div class="protein-badge">
      <span class="protein-amount">20 G</span>
      <span class="protein-label">PROTEIN</span>
    </div>
    <div class="flavour-photo" role="img" aria-label="Photo of two halved fresh lemons">
      <div class="photo-half back"></div>
      <div class="photo-half front"></div>
    </div>
  </div>
</body>
</html>
```